Infographic comparing two personal financial success strategies

Need an infographic designed comparing typical financial planning advice to my proprietary wealth platform "The Brightward Path Method". My system is designed primarily for business owners, professionals and executives who aspire to a work-optional lifestyle. I would like designs that use my websites color palette (www.corvenmq.com) and include my logo. The final design should highlight the differences between the typical approach and the benefits of the "The Brightward Path Method".

Target Market(s)

Business owners, professionals (doctors, lawyers, accoutnants, and business executives

Industry/Entity Type

Financial Service

Font styles to use
Sans Serif

Colors
33a6d7
0455a3
cee9f5

```html
<!DOCTYPE html>
<html lang="en">
<head>
<meta charset="utf-8">
<title>The Brightward Path Method</title>
<link href="https://fonts.googleapis.com/css2?family=Open+Sans:wght@400;600;700;800&family=Libre+Baskerville&display=swap" rel="stylesheet">
<style>
:root{
  --navy:#0d2a63;
  --navy-mid:#1a4f9c;
  --ink:#1b2e5e;
  --sky:#33a6d7;
  --royal:#0455a3;
  --pale:#cee9f5;
  --canvas:#eef7fc;
  --band:#f4f6f7;
  --grey-arrow:#9fb6be;
  --icon:#557a93;
}
*{margin:0;padding:0;box-sizing:border-box}
html,body{width:1200px;height:2628px;overflow:hidden}
body{position:relative;background:var(--canvas);font-family:"Open Sans",Arial,sans-serif;color:var(--ink)}
.header{position:absolute;left:0;top:0;width:1200px;height:422px;background:linear-gradient(135deg,#2260aa 0%,var(--navy-mid) 35%,var(--navy) 100%)}
.brand{position:absolute;left:52px;top:52px;display:flex;align-items:center;gap:18px;color:#fff}
.brand-dot{width:88px;height:88px;border-radius:50%;border:6px solid #fff}
.brand-name{font-size:40px;font-weight:800;letter-spacing:.5px;line-height:1}
.brand-tag{font-size:27px;font-weight:400;margin-top:6px;line-height:1}
.title{position:absolute;left:52px;top:205px;width:760px;color:#fff;font-family:"Libre Baskerville",Georgia,serif;line-height:1;font-weight:400}
.title .small{font-size:56px;display:block;white-space:nowrap}
.title .big{font-size:80px;display:block;margin-top:18px;white-space:nowrap}
.header-badge{position:absolute;left:836px;top:56px;width:308px;height:308px;border-radius:50%;background:#fff;display:flex;align-items:center;justify-content:center}
.header-badge-art{width:266px;height:266px;border-radius:50%;background:linear-gradient(135deg,#2466b0,#123c80)}
.compare{position:absolute;left:0;top:422px;width:1200px;height:210px;background:var(--band)}
.stage{position:absolute;left:0;top:0}
.label{position:absolute;font-weight:700;color:#fff;text-align:center;line-height:1.2;text-transform:uppercase}
.compare-left{left:100px;top:525px;width:250px;font-size:24px}
.compare-right{left:848px;top:525px;width:250px;font-size:24px}
.vs{position:absolute;left:549px;top:536px;width:94px;text-align:center;font-size:30px;font-weight:700;color:#fff}
.item{position:absolute;width:330px}
.item h3{font-size:21px;font-weight:800;color:var(--ink);text-transform:uppercase;line-height:1.2}
.item .sub{font-size:14px;font-weight:800;text-transform:uppercase;line-height:1.45;margin-top:4px}
.item p{font-size:18px;line-height:1.4;margin-top:4px}
.left{left:56px}
.right{left:660px;width:320px}
.right h3{color:var(--sky)}
.check{display:flex;gap:10px;align-items:flex-start;font-size:18px;line-height:1.35;margin-top:12px}
.check.indent{margin-left:22px}
.tick{flex:none;width:14px;height:14px;border:1.5px solid var(--sky);border-radius:50%;position:relative;margin-top:5px}
.tick::after{content:"";position:absolute;left:3px;top:1px;width:4px;height:7px;border:solid var(--sky);border-width:0 1.5px 1.5px 0;transform:rotate(45deg)}
.list{font-size:18px;line-height:1.4;margin-top:14px}
.list li{list-style:none;margin-top:18px}
.icon{position:absolute;border-radius:18px;background:var(--icon);opacity:.85}
.growth-art{position:absolute;left:657px;top:2181px;width:440px;height:355px;border-radius:40px 40px 20px 20px;background:linear-gradient(180deg,#c7d7df 0%,#8fa9b6 100%)}
.footer{position:absolute;left:0;top:2584px;width:1200px;height:44px;background:var(--navy)}
</style>
</head>
<body>
<header class="header">
  <div class="brand">
    <div class="brand-dot"></div>
    <div>
      <div class="brand-name">CORVEN MERIDIAN FINANCIAL</div>
      <div class="brand-tag">Live life on your terms</div>
    </div>
  </div>
  <h1 class="title"><span class="small">THE BRIGHTWARD</span><span class="big">PATH METHOD</span></h1>
  <div class="header-badge"><div class="header-badge-art" role="img" aria-label="Icon of open hands holding a house, a family and a money bag"></div></div>
</header>
<div class="compare"></div>

<svg class="stage" width="1200" height="2628" viewBox="0 0 1200 2628">
  <path d="M0 622 Q15 640 30 622 T60 622 T90 622 T120 622 T150 622 T180 622 T210 622 T240 622 T270 622 T300 622 T330 622 T360 622 T390 622 T420 622 T450 622 T480 622 T510 622 T540 622 T570 622 T600 622 T630 622 T660 622 T690 622 T720 622 T750 622 T780 622 T810 622 T840 622 T870 622 T900 622 T930 622 T960 622 T990 622 T1020 622 T1050 622 T1080 622 T1110 622 T1140 622 T1170 622 T1200 622 V600 H0Z" fill="#fff"/>
  <path d="M53 552 L112 495 V515 H394 V589 H112 V609Z" fill="var(--grey-arrow)"/>
  <path d="M1148 552 L1089 495 V515 H806 V589 H1089 V609Z" fill="var(--grey-arrow)"/>
  <circle cx="464" cy="552" r="82" fill="var(--navy)"/>
  <rect x="434" y="515" width="56" height="70" rx="5" fill="none" stroke="#fff" stroke-width="5"/>
  <g stroke="#fff" stroke-width="5" stroke-linecap="round">
    <line x1="446" y1="532" x2="451" y2="532"/><line x1="460" y1="532" x2="478" y2="532"/>
    <line x1="446" y1="548" x2="451" y2="548"/><line x1="460" y1="548" x2="478" y2="548"/>
    <line x1="446" y1="564" x2="451" y2="564"/><line x1="460" y1="564" x2="470" y2="564"/>
    <line x1="497" y1="588" x2="508" y2="599"/>
  </g>
  <circle cx="488" cy="578" r="12" fill="var(--navy)" stroke="#fff" stroke-width="5"/>
  <circle cx="596" cy="552" r="47" fill="var(--grey-arrow)"/>
  <circle cx="718" cy="552" r="82" fill="var(--sky)"/>
  <circle cx="718" cy="552" r="36" fill="none" stroke="#fff" stroke-width="7"/>
  <circle cx="718" cy="552" r="17" fill="none" stroke="#fff" stroke-width="6"/>
  <g stroke="#fff" stroke-width="7"><line x1="718" y1="516" x2="718" y2="535"/><line x1="718" y1="569" x2="718" y2="588"/><line x1="682" y1="552" x2="701" y2="552"/><line x1="735" y1="552" x2="754" y2="552"/></g>

  <line x1="413" y1="780" x2="413" y2="2523" stroke="var(--ink)" stroke-width="2"/>
  <g fill="none" stroke="var(--sky)" stroke-width="3" stroke-dasharray="3 5">
    <path d="M432 818 H525 V729 H632"/>
    <path d="M432 1028 H525 V939 H632"/>
    <path d="M432 1302 H525 V1212 H632"/>
    <path d="M432 1524 H525 V1438 H632"/>
    <path d="M432 1924 H525 V1840 H632"/>
    <path d="M432 2137 H525 V2048 H632"/>
  </g>
  <g fill="none" stroke="var(--sky)" stroke-width="4" stroke-linecap="round" stroke-linejoin="round">
    <path d="M624 719 L636 729 L624 739"/><path d="M624 929 L636 939 L624 949"/>
    <path d="M624 1202 L636 1212 L624 1222"/><path d="M624 1428 L636 1438 L624 1448"/>
    <path d="M624 1830 L636 1840 L624 1850"/><path d="M624 2038 L636 2048 L624 2058"/>
  </g>
  <g fill="none" stroke="var(--ink)" stroke-width="3" stroke-dasharray="3 5">
    <path d="M394 827 H272"/><path d="M394 1037 H272"/><path d="M394 1302 H272"/><path d="M394 1524 H272"/>
    <path d="M394 1931 H272"/><path d="M394 2141 H272"/><path d="M394 2367 H272"/><path d="M394 2507 H272"/>
  </g>
  <g fill="none" stroke="var(--ink)" stroke-width="4" stroke-linecap="round" stroke-linejoin="round">
    <path d="M272 817 L260 827 L272 837"/><path d="M272 1027 L260 1037 L272 1047"/>
    <path d="M272 1292 L260 1302 L272 1312"/><path d="M272 1514 L260 1524 L272 1534"/>
    <path d="M272 1921 L260 1931 L272 1941"/><path d="M272 2131 L260 2141 L272 2151"/>
    <path d="M272 2357 L260 2367 L272 2377"/><path d="M272 2497 L260 2507 L272 2517"/>
  </g>
  <g fill="var(--ink)" stroke="#c9d6e6" stroke-width="4">
    <circle cx="413" cy="818" r="19"/><circle cx="413" cy="1028" r="19"/><circle cx="413" cy="1302" r="19"/><circle cx="413" cy="1524" r="19"/>
    <circle cx="413" cy="1924" r="19"/><circle cx="413" cy="2137" r="19"/><circle cx="413" cy="2365" r="19"/><circle cx="413" cy="2505" r="19"/>
  </g>
  <g fill="#fff" font-family="Open Sans, Arial, sans-serif" font-size="18" font-weight="700" text-anchor="middle">
    <text x="413" y="824">1</text><text x="413" y="1034">2</text><text x="413" y="1308">3</text><text x="413" y="1530">4</text>
    <text x="413" y="1930">5</text><text x="413" y="2143">6</text><text x="413" y="2371">7</text><text x="413" y="2511">8</text>
  </g>
</svg>

<div class="label compare-left">Typical Financial Advice</div>
<div class="label compare-right">Brightward Path Method ™</div>
<div class="vs">VS</div>

<div class="item left" style="top:815px"><h3>Make Income</h3><p>Job, Company, Real-Estate,<br>Investments, etc.</p></div>
<div class="item left" style="top:1025px"><h3>Pay Taxes</h3><p>Reduces income</p><div class="check"><span class="tick"></span>RRSP</div></div>
<div class="item left" style="top:1290px"><h3>Pay Interest</h3><div class="sub">( Mortgage, Car Loan,<br>Credit Cards, etc. )</div><p>Reduces income</p><div class="check"><span class="tick"></span>Pay off faster</div></div>
<div class="item left" style="top:1512px"><h3>Pay for Lifestyle</h3><div class="sub">( Food, Shelter, Vacations,<br>Recreation, Education, etc. )</div><p>Reduces income</p><div class="check"><span class="tick"></span>Cut back on spending</div></div>
<div class="item left" style="top:1919px"><h3>Hope For</h3><p>good returns on what you can save</p></div>
<div class="item left" style="top:2129px"><h3>Hope Nothing</h3><p>Bad happens</p><div class="check"><span class="tick"></span>Laid-off, no work, fired,<br>company fails, etc.</div><div class="check"><span class="tick"></span>Can’t work for health reason(s)</div></div>
<div class="item left" style="top:2355px"><h3>Hope You Don’t</h3><p>live too long in retirement</p></div>
<div class="item left" style="top:2495px"><h3>Minimizes Future</h3><p>lifestyle and dreams</p></div>

<div class="item right" style="top:717px"><h3>Cash Flow</h3><p>Job, Company, Real-Estate,<br>Investments, etc.</p></div>
<div class="item right" style="top:927px"><h3>Cash Flow Maximization</h3><p>Get the most from your money now, don’t reduce lifestyle</p>
  <div class="check"><span class="tick"></span>Reduce taxes – Flow-through,<br>RRSPs &amp; TFSAs</div>
  <div class="check"><span class="tick"></span>Recapture Interest expense – Use Opportunity Cost</div></div>
<div class="item right" style="top:1200px"><h3>Cash Flow Protection</h3><p>Protect &amp; Multiple the uses of your money</p>
  <div class="check"><span class="tick"></span>Protect your income</div>
  <div class="check"><span class="tick"></span>Create guaranteed savings</div></div>
<div class="item right" style="top:1426px"><h3>Cash Flow Expansion</h3><p>Multiple your income streams and increase cash flow now</p>
  <div class="check"><span class="tick"></span>Regularly add new income streams</div>
  <div class="check indent"><span class="tick"></span>Dividend and interest paying investments</div>
  <ol class="list"><li>1. Direct &amp; In-direct Real-estate</li><li>2. Private Business ownership</li><li>3. Company Stocks</li><li>4. Private Lending</li></ol></div>
<div class="item right" style="top:1828px"><h3>Work Because</h3><p>you want to…not because you have to!</p></div>
<div class="item right" style="top:2036px"><h3>Bluesky Think</h3><p>your goals, dreams and life!</p></div>

<div class="icon" style="left:1025px;top:692px;width:120px;height:105px" role="img" aria-label="Hand holding a dollar sign"></div>
<div class="icon" style="left:1030px;top:960px;width:100px;height:144px" role="img" aria-label="Hand with a dollar card"></div>
<div class="icon" style="left:1012px;top:1218px;width:136px;height:114px" role="img" aria-label="Hand holding a percent sign"></div>
<div class="icon" style="left:1030px;top:1550px;width:110px;height:106px" role="img" aria-label="Hand holding banknotes"></div>
<div class="icon" style="left:1030px;top:1822px;width:92px;height:88px" role="img" aria-label="House"></div>
<div class="icon" style="left:1025px;top:2024px;width:110px;height:78px" role="img" aria-label="Hand with currency coins"></div>
<div class="growth-art" role="img" aria-label="Illustration of an open hand holding a growing sprout"></div>

<footer class="footer"></footer>
</body>
</html>
```